Established food business needs a new name card design

Refer to attached current name card. Would like a new professional look design with only the company name and logo without any pictures. Would like green and yellow to be included.
To include:
My name "IBRAHIM SUKRI" and hand phone number "87260413".
To delete "
"Along Brackendale Ave 8" and
"www.nur-tiwas.com.sg"
To change email to:
"tkr27@velmorix.com.sg"

```html
<!DOCTYPE html>
<html lang="en">
<head>
<meta charset="utf-8">
<title>Nur-Tiwas Eating Corner – Name Card</title>
<link rel="stylesheet" href="https://fonts.googleapis.com/css2?family=Montserrat:wght@300;700;800&family=Roboto:wght@300;400&display=swap">
<style>
  :root {
    --green: #0e4a30;
    --yellow: #f2c314;
    --white: #ffffff;
    --backdrop: #e3e7e5;
    --ink: #0e4a30;
  }
  * { margin: 0; padding: 0; box-sizing: border-box; }
  html, body { width: 1200px; height: 900px; overflow: hidden; }
  body {
    background: var(--backdrop);
    font-family: "Roboto", Arial, sans-serif;
    position: relative;
  }
  .card {
    position: absolute;
    left: 250px;
    width: 700px;
    height: 400px;
    overflow: hidden;
    box-shadow: 0 6px 18px rgba(0,0,0,0.18);
  }
  .card-front {
    top: 35px;
    background: var(--green);
    display: flex;
    align-items: center;
    justify-content: center;
  }
  .card-back { top: 465px; background: var(--white); }
  .card-art { position: absolute; inset: 0; width: 100%; height: 100%; }

  .brand {
    display: flex;
    align-items: center;
    gap: 18px;
  }
  .brand-mark {
    border: 6px solid var(--yellow);
    border-radius: 50%;
    flex: none;
  }
  .brand-name {
    font-family: "Montserrat", Arial, sans-serif;
    font-weight: 800;
    color: var(--yellow);
    letter-spacing: 1px;
    line-height: 1;
  }
  .brand-tagline {
    font-family: "Montserrat", Arial, sans-serif;
    font-weight: 300;
    color: var(--yellow);
    letter-spacing: 5px;
    margin-top: 6px;
    padding-top: 6px;
    border-top: 1px solid var(--yellow);
  }
  .card-front .brand-mark { width: 110px; height: 110px; border-width: 9px; }
  .card-front .brand-name { font-size: 58px; }
  .card-front .brand-tagline { font-size: 19px; letter-spacing: 8px; }

  .card-back .brand { position: absolute; left: 34px; top: 44px; gap: 12px; }
  .card-back .brand-mark { width: 62px; height: 62px; }
  .card-back .brand-name { font-size: 31px; }
  .card-back .brand-tagline { font-size: 11px; margin-top: 4px; padding-top: 4px; }

  .holder-name {
    position: absolute;
    right: 40px;
    top: 176px;
    font-family: "Montserrat", Arial, sans-serif;
    font-weight: 800;
    font-size: 28px;
    color: var(--ink);
    letter-spacing: 0.5px;
  }
  .divider {
    position: absolute;
    left: 170px;
    right: 40px;
    top: 222px;
    height: 2px;
    background: var(--ink);
  }
  .contacts {
    position: absolute;
    right: 40px;
    top: 236px;
    list-style: none;
    text-align: right;
    color: var(--ink);
    font-size: 15px;
    font-weight: 300;
  }
  .contacts li {
    display: flex;
    justify-content: flex-end;
    align-items: center;
    gap: 8px;
    height: 26px;
  }
  .contact-icon {
    width: 16px; height: 16px;
    border-radius: 50%;
    background: var(--ink);
    display: inline-flex;
    align-items: center;
    justify-content: center;
  }
  .address {
    position: absolute;
    left: 40px;
    top: 288px;
    color: var(--ink);
    font-size: 14px;
    font-weight: 300;
    line-height: 1.45;
  }
</style>
</head>
<body>

<section class="card card-front" aria-label="Name card front">
  <div class="brand">
    <span class="brand-mark"></span>
    <div>
      <div class="brand-name">NUR-TIWAS</div>
      <div class="brand-tagline">EATING CORNER</div>
    </div>
  </div>
</section>

<section class="card card-back" aria-label="Name card back">
  <svg class="card-art" viewBox="0 0 700 400" preserveAspectRatio="none" aria-hidden="true">
    <path d="M0,0 H700 V24 C610,24 520,24 470,70 C420,120 380,168 0,172 Z" fill="var(--green)"/>
    <path d="M0,186 C385,182 430,132 482,82 C530,38 610,36 700,36" fill="none" stroke="var(--yellow)" stroke-width="9"/>
    <path d="M0,199 C395,195 442,145 492,95" fill="none" stroke="var(--yellow)" stroke-width="3"/>
    <rect x="0" y="378" width="420" height="22" fill="var(--yellow)"/>
    <rect x="420" y="378" width="280" height="22" fill="var(--green)"/>
  </svg>

  <div class="brand">
    <span class="brand-mark"></span>
    <div>
      <div class="brand-name">NUR-TIWAS</div>
      <div class="brand-tagline">EATING CORNER</div>
    </div>
  </div>

  <h1 class="holder-name">IBRAHIM SUKRI</h1>
  <div class="divider"></div>

  <ul class="contacts">
    <li>87260413
      <span class="contact-icon"><svg width="10" height="10" viewBox="0 0 10 10"><path d="M2,1 L4,1 L4.6,3 L3.5,3.8 C4,5 5,6 6.2,6.5 L7,5.4 L9,6 L9,8 C5,8.5 1.5,5 2,1 Z" fill="#fff"/></svg></span>
    </li>
    <li>tkr27@velmorix.com.sg
      <span class="contact-icon"><svg width="10" height="10" viewBox="0 0 10 10"><rect x="1" y="2.5" width="8" height="5.5" fill="#fff"/><path d="M1,2.5 L5,5.6 L9,2.5" fill="none" stroke="var(--green)" stroke-width="0.9"/></svg></span>
    </li>
  </ul>

  <p class="address">18 Kelvale Industrial Estate<br>Road 2 # 02-07 Singapore 728140</p>
</section>

</body>
</html>
```